Courier Business needs a Business Card Design !!!

My new company needs a business card design. Our company name is Swift Heron Courier & Delivery Services. We will be servicing residential , government and business clients in the City of Yellowknife, Northwest Territories, Canada. I would like the following information included on the card: Name- Walter Pruitt. Title- Owner. Company- Swift Heron Courier & Delivery Services. Address- PO Box 5918 , Yellowknife , NWT, X1A 4K3. Phone- 867-392-7184. Email- swiftheroncourieryk@mailbox-example.net. Facebook- www.socialpage-example.net/swiftheroncourieryk. I would like my double sided card to be the standard size of 84mm x 55mm. No borders. Use CMYK mode.1039x 697 pixels at least. I would like my logo to take up at least one quarter of the area of one side of the card. Text should be at least 8 point with perhaps my name being 10 point and my company name being 12-15 point . It should have clear readable font. Please use one or two bold colors. I am trying to attract the business community so a professional look might be best. My tag line is " On Time Every Time ". Nice safe margins please. We will be providing fast, reliable and professional delivery of envelopes and small packages within the City of Yellowknife. We offer 100% satisfaction or a complete refund. I have included a file of our logo. I like black, blue and red but am willing to look at what you feel would work best. I do not really like white as a background color.

Target Market(s)

Professionals , business owners. 30-50 years old

Industry/Entity Type

Residential

Contact Information for Business Card

As noted in brief

Font styles to use
Serif
Sans Serif

Colors
000000
0255a3
f04a50

Requirements
Must have
• My contact info. My logo
Nice to have
• Simple elegant design but still catches the eye
Should not have
• White background color

```html
<!DOCTYPE html>
<html lang="en">
<head>
<meta charset="utf-8">
<title>Swift Heron Courier &amp; Delivery Services – Business Card</title>
<link href="https://fonts.googleapis.com/css2?family=Arimo:ital,wght@0,400;0,700;1,400&display=swap" rel="stylesheet">
<style>
  :root {
    --bg: #b9bcc0;
    --card: #050505;
    --red: #f04a50;
    --blue: #0255a3;
    --text: #d9d9d9;
    --muted: #a6a6a6;
  }
  html, body {
    margin: 0;
    width: 1200px;
    height: 900px;
    overflow: hidden;
    background: var(--bg);
    font-family: "Arimo", Arial, sans-serif;
  }
  .stage {
    position: relative;
    width: 1200px;
    height: 900px;
  }
  .card {
    position: absolute;
    left: 290px;
    width: 620px;
    height: 406px;
    background: var(--card);
    box-shadow: 0 10px 30px rgba(0,0,0,0.35);
    overflow: hidden;
  }
  .card--back { top: 32px; }
  .card--front { top: 462px; }

  /* Back side */
  .back-brand {
    position: absolute;
    right: 50px;
    top: 150px;
    width: 300px;
    color: var(--red);
    font-weight: 700;
    font-size: 30px;
    line-height: 1.1;
    text-transform: uppercase;
    text-align: left;
  }

  /* Front side */
  .chevron {
    position: absolute;
    left: 24px;
    top: 30px;
  }
  .holder {
    position: absolute;
    left: 70px;
    top: 30px;
  }
  .holder__name {
    margin: 0;
    color: var(--red);
    font-size: 26px;
    font-weight: 400;
  }
  .holder__title {
    margin: 2px 0 0;
    color: var(--muted);
    font-size: 22px;
    font-style: italic;
  }
  .contacts {
    position: absolute;
    left: 70px;
    top: 122px;
    margin: 0;
    padding: 0;
    list-style: none;
    color: var(--text);
    font-size: 16px;
    line-height: 22px;
  }
  .contacts li {
    display: flex;
    align-items: flex-start;
  }
  .contacts .icon {
    flex: 0 0 18px;
    width: 18px;
    height: 18px;
    margin: 2px 12px 0 0;
    fill: var(--red);
  }
  .front-brand {
    position: absolute;
    right: 34px;
    top: 30px;
    width: 250px;
    color: var(--red);
    font-weight: 700;
    font-size: 21px;
    line-height: 1.1;
    text-transform: uppercase;
  }
  .tagline {
    position: absolute;
    right: 40px;
    bottom: 34px;
    margin: 0;
    color: var(--blue);
    font-size: 24px;
    letter-spacing: 0.5px;
    text-transform: uppercase;
  }
</style>
</head>
<body>
<main class="stage">

  <section class="card card--back" aria-label="Business card back">
    <div class="back-brand">Swift Heron<br>Courier &amp; Delivery Services</div>
  </section>

  <section class="card card--front" aria-label="Business card front">
    <svg class="chevron" width="22" height="40" viewBox="0 0 22 40" aria-hidden="true">
      <polyline points="4,4 18,20 4,36" fill="none" stroke="var(--blue)" stroke-width="4"/>
    </svg>

    <div class="holder">
      <h1 class="holder__name">Walter Pruitt</h1>
      <p class="holder__title">Owner</p>
    </div>

    <ul class="contacts">
      <li>
        <svg class="icon" viewBox="0 0 18 18" aria-hidden="true"><path d="M9 2 1 9h2.5v7h4v-4.5h3V16h4V9H17z"/></svg>
        <span>PO Box 5918 , Yellowknife ,<br>NWT, X1A 4K3</span>
      </li>
      <li>
        <svg class="icon" viewBox="0 0 18 18" aria-hidden="true"><path d="M5 1h8a1.5 1.5 0 0 1 1.5 1.5v13A1.5 1.5 0 0 1 13 17H5a1.5 1.5 0 0 1-1.5-1.5v-13A1.5 1.5 0 0 1 5 1zm0 2v10h8V3zm4 11a1 1 0 1 0 0 2 1 1 0 0 0 0-2z"/></svg>
        <span>867-392-7184</span>
      </li>
      <li>
        <svg class="icon" viewBox="0 0 18 18" aria-hidden="true"><path d="M1 4h16v11H1zm1.6 1.3L9 10.2l6.4-4.9z"/></svg>
        <span>swiftheroncourieryk@mailbox-example.net</span>
      </li>
      <li>
        <svg class="icon" viewBox="0 0 18 18" aria-hidden="true"><rect x="2" y="2" width="14" height="14" rx="2"/></svg>
        <span>www.socialpage-example.net/swiftheroncourieryk</span>
      </li>
    </ul>

    <div class="front-brand">Swift Heron<br>Courier &amp; Delivery Services</div>

    <p class="tagline">On Time Every Time</p>
  </section>

</main>
</body>
</html>
```